Brightmoor Signal needs a Business Card

Designers!
More often than not, people want a cheap business card and often argue "I only want 100, not 500" - Years ago I worked in print and always wanted a client to ask for something that challenged me and would be great for my portfolio.

Years have past, and I dont have the time to do it myself so I'd love to see what everyone can offer.

Reason: Hey Guys, The designs are looking good but i've extended it a few more days as I wont be near a laptop and i'm trying to provide everyone feedback - Sorry!

Target Market(s)

Key decision makers, Potential Clients, Networking events and opportunities.

Industry/Entity Type

Business

Requirements
Must have
• Typography is very important. The type of paper is important.
The print, the shape. The creativity.
I'm very inspired by the below link
http://www.palevantro.com/blog/business-card-design/

Nice to have
• Stencelled cutouts. Embossing, nice typography.
I'd like the business card to be a conversation piece itself.

Attached is an image of business cards i've had in the past.
Additionally, some logos i've recently had designed by Quillmarsh.

```html
<!DOCTYPE html>
<html lang="en">
<head>
<meta charset="utf-8">
<title>Brightmoor Signal – Business Card</title>
<link href="https://fonts.googleapis.com/css2?family=Advent+Pro:wght@300;400&family=Montserrat:wght@500&family=Questrial&display=swap" rel="stylesheet">
<style>
  :root {
    --bg: #3a3a3a;
    --green: #8fc33c;
    --paper: #f1f0ec;
    --navy: #2c3868;
    --rule: #9cc95a;
  }
  * { box-sizing: border-box; margin: 0; padding: 0; }
  html, body { width: 1200px; height: 751px; overflow: hidden; }
  body { background: var(--bg); position: relative; font-family: "Questrial", sans-serif; color: var(--navy); }

  .card {
    position: absolute;
    width: 752px; height: 358px;
    background: var(--green);
    padding: 22px;
  }
  .card__paper { width: 100%; height: 100%; background: var(--paper); position: relative; overflow: hidden; }

  .card--front { left: 40px; top: 40px; }
  .card--back { left: 398px; top: 333px; }

  /* front */
  .brand { position: absolute; left: 0; right: 0; top: 118px; text-align: center; }
  .brand__name {
    display: inline-flex; align-items: center; gap: 14px;
    font-size: 38px; letter-spacing: 1px;
    color: var(--navy); text-transform: uppercase;
  }
  .brand__square { width: 30px; height: 30px; background: var(--navy); display: inline-block; }
  .brand__rule { width: 330px; height: 1px; background: var(--rule); margin: 12px auto 6px; }
  .brand__url { font-size: 14px; letter-spacing: 5.5px; color: var(--green); }

  /* back */
  .person { position: absolute; left: 36px; top: 44px; width: 300px; }
  .person__name { font-family: "Montserrat", sans-serif; font-weight: 500; font-size: 23px; letter-spacing: 1.3px; text-transform: uppercase; padding-left: 4px; white-space: nowrap; }
  .person__rule { height: 2px; background: var(--rule); margin: 8px 0 6px; }
  .person__role { font-size: 25px; letter-spacing: .5px; white-space: nowrap; }

  .contact { position: absolute; left: 396px; top: 32px; width: 290px; }
  .contact__row { display: flex; align-items: center; gap: 8px; border-bottom: 1.5px solid var(--rule); white-space: nowrap; }
  .contact__row--phone { height: 58px; padding-bottom: 4px; gap: 6px; }
  .contact__row--web { height: 34px; }
  .contact__row--social { height: 52px; }
  .contact__row--mail { height: 40px; }
  .contact__phone { font-family: "Advent Pro", sans-serif; font-weight: 300; font-size: 46px; letter-spacing: 0; line-height: 1; }
  .contact__web { font-size: 17px; letter-spacing: .4px; }
  .contact__social { font-size: 21px; letter-spacing: 2.5px; }
  .contact__mail { font-family: "Advent Pro", sans-serif; font-size: 19px; letter-spacing: .5px; text-transform: uppercase; }
  .contact__dot { width: 26px; height: 26px; border-radius: 50%; background: var(--navy); flex: none; }
  .contact__address { display: flex; gap: 8px; margin-top: 10px; font-size: 17px; letter-spacing: 1.2px; line-height: 1.25; text-transform: uppercase; white-space: nowrap; }
  .icon { flex: none; fill: var(--navy); }
</style>
</head>
<body>

<section class="card card--front">
  <div class="card__paper">
    <div class="brand">
      <div class="brand__name"><span class="brand__square"></span>Brightmoor Signal</div>
      <div class="brand__rule"></div>
      <div class="brand__url">brightmoorsignal.com.au</div>
    </div>
  </div>
</section>

<section class="card card--back">
  <div class="card__paper">
    <div class="person">
      <div class="person__name">Dorian Halvecke</div>
      <div class="person__rule"></div>
      <div class="person__role">Consultant &amp; Educator</div>
    </div>

    <div class="contact">
      <div class="contact__row contact__row--phone">
        <svg class="icon" width="44" height="40" viewBox="0 0 50 44" aria-hidden="true">
          <path d="M4 14 C4 4 46 4 46 14 L46 18 L36 18 L35 12 L15 12 L14 18 L4 18 Z"/>
          <path d="M14 20 L36 20 L44 40 L6 40 Z"/>
          <circle cx="25" cy="30" r="6" fill="#f1f0ec"/>
          <circle cx="25" cy="30" r="3"/>
        </svg>
        <span class="contact__phone">555.382.9140</span>
      </div>
      <div class="contact__row contact__row--web">
        <svg class="icon" width="18" height="18" viewBox="0 0 18 18" aria-hidden="true">
          <circle cx="9" cy="9" r="8"/>
          <path d="M1 9h16M9 1c-4 4-4 12 0 16M9 1c4 4 4 12 0 16" stroke="#f1f0ec" stroke-width="1.2" fill="none"/>
        </svg>
        <span class="contact__web">www.thetuitionhelper.org</span>
      </div>
      <div class="contact__row contact__row--social">
        <span class="contact__dot"></span>
        <span class="contact__social">@TheTuitionPro</span>
      </div>
      <div class="contact__row contact__row--mail">
        <span class="contact__mail">dorian@thetuitionhelper.org</span>
      </div>
      <div class="contact__address">
        <svg class="icon" width="14" height="20" viewBox="0 0 14 20" aria-hidden="true">
          <path d="M7 0C3 0 0 3 0 7c0 5 7 13 7 13s7-8 7-13c0-4-3-7-7-7z"/>
          <circle cx="7" cy="7" r="2.6" fill="#f1f0ec"/>
        </svg>
        <span>1180 W. Larchmont Ave<br>Suite C, Fenwick, CA 90000</span>
      </div>
    </div>
  </div>
</section>

</body>
</html>
```